Dental Office Business Card

We need a business card for our pediatric dentistry office.
On one side the design needs to contain the following:
our logo (attached)
Corvin Pediatric Smiles
Tamsin Vetrakovich, DDS
Board Certified Pediatric Dentist
Tel: (617) 555-0148)
Fax: (617) 555-0193
Email: info@corvinpediatricsmiles.example
Web: www.corvinpediatricsmiles.example
Address: 42 Brambury Ln, Suite 208, Wellesley, MA 02481

On the other side of the card, the design needs to have an appointment reminder (date and time as well as day of the week) similar to the design attached (no need for appointment reason “For”)

```html
<!DOCTYPE html>
<html lang="en">
<head>
<meta charset="utf-8">
<title>Corvin Pediatric Smiles – Business Card</title>
<link rel="stylesheet" href="https://fonts.googleapis.com/css2?family=Cinzel:wght@500&family=Montserrat:wght@400;500;700;800&display=swap">
<style>
  :root {
    --backdrop: #1c1c1e;
    --card: #ffffff;
    --ink: #1a1a1a;
    --ink-soft: #333333;
    --mint: #a8d8a6;
    --mint-deep: #8fcb8c;
    --rule-grey: #dcdcdc;
  }
  * { box-sizing: border-box; margin: 0; padding: 0; }
  html, body { width: 1200px; height: 947px; overflow: hidden; }
  body {
    background: var(--backdrop);
    font-family: "Montserrat", sans-serif;
    color: var(--ink);
    position: relative;
  }
  .card {
    position: absolute;
    top: 319px;
    width: 540px;
    height: 309px;
    background: var(--card);
    border-radius: 16px;
    overflow: hidden;
  }
  .card--reminder { left: 40px; }
  .card--contact { left: 620px; }

  /* Reminder side */
  .reminder-title {
    position: absolute;
    top: 46px;
    left: 0; right: 0;
    text-align: center;
  }
  .reminder-title__main {
    font-family: "Cinzel", serif;
    font-weight: 500;
    font-size: 36px;
    letter-spacing: 1px;
    line-height: 1;
  }
  .reminder-title__sub {
    font-family: "Montserrat", sans-serif;
    font-weight: 800;
    font-size: 17px;
    letter-spacing: 3px;
    margin-top: 4px;
    padding-left: 60px;
  }
  .fill-row {
    position: absolute;
    top: 148px;
    left: 36px;
    right: 30px;
    display: flex;
    align-items: flex-end;
    font-size: 17px;
    font-weight: 500;
  }
  .fill-row__line {
    border-bottom: 1.2px solid var(--ink);
    height: 18px;
    margin: 0 6px;
  }
  .fill-row__line--date { flex: 1.6; }
  .fill-row__line--time { flex: 1; }
  .weekday-row {
    position: absolute;
    top: 214px;
    left: 36px;
    right: 24px;
    display: flex;
    justify-content: space-between;
    font-size: 16px;
    font-weight: 500;
  }
  .weekday { display: flex; align-items: center; gap: 6px; }
  .weekday__box {
    width: 17px; height: 14px;
    border: 1.4px solid var(--mint-deep);
    border-radius: 4px;
  }

  /* Contact side */
  .brand {
    position: absolute;
    left: 30px;
    top: 120px;
    display: flex;
    align-items: center;
    gap: 10px;
  }
  .brand__dot {
    width: 32px; height: 32px;
    border-radius: 50%;
    background: var(--mint);
    flex: none;
  }
  .brand__name {
    font-weight: 700;
    font-size: 19px;
    line-height: 1.15;
    color: var(--ink);
  }
  .details {
    position: absolute;
    left: 268px;
    top: 40px;
    width: 262px;
  }
  .details__name {
    font-weight: 700;
    font-size: 18px;
    color: var(--mint-deep);
    line-height: 1.2;
  }
  .details__title {
    font-size: 11.5px;
    color: var(--ink-soft);
    margin-top: 2px;
  }
  .details__address {
    font-size: 11.5px;
    color: var(--ink-soft);
    margin-top: 14px;
    line-height: 1.4;
  }
  .details__contacts {
    list-style: none;
    margin-top: 10px;
    font-size: 11.5px;
    color: var(--ink-soft);
    line-height: 1.55;
  }
  .details__contacts li { display: flex; align-items: center; gap: 7px; }
  .details__contacts svg { width: 11px; height: 11px; fill: var(--mint-deep); flex: none; }
  .swoosh { position: absolute; left: 0; top: 0; }
  .website {
    position: absolute;
    left: 318px;
    top: 278px;
    font-size: 11.5px;
    line-height: 1;
    white-space: nowrap;
    color: var(--ink-soft);
    transform: rotate(-27deg);
    transform-origin: left bottom;
  }
</style>
</head>
<body>

<section class="card card--reminder" aria-label="Appointment reminder side">
  <div class="reminder-title">
    <div class="reminder-title__main">APPOINTMENT</div>
    <div class="reminder-title__sub">REMINDER</div>
  </div>
  <div class="fill-row">
    <span>Date:</span><span class="fill-row__line fill-row__line--date"></span>
    <span>Time:</span><span class="fill-row__line fill-row__line--time"></span>
    <span>am/pm</span>
  </div>
  <div class="weekday-row">
    <span class="weekday"><span class="weekday__box"></span>Mon</span>
    <span class="weekday"><span class="weekday__box"></span>Tue</span>
    <span class="weekday"><span class="weekday__box"></span>Wed</span>
    <span class="weekday"><span class="weekday__box"></span>Thur</span>
    <span class="weekday"><span class="weekday__box"></span>Fri</span>
    <span class="weekday"><span class="weekday__box"></span>Sat</span>
    <span class="weekday"><span class="weekday__box"></span>Sat</span>
  </div>
</section>

<section class="card card--contact" aria-label="Contact side">
  <svg class="swoosh" width="540" height="309" viewBox="0 0 540 309" aria-hidden="true">
    <path d="M250 309 C 330 200, 430 150, 540 118" fill="none" stroke="var(--rule-grey)" stroke-width="6"/>
    <path d="M272 309 C 350 210, 440 165, 540 130 L540 309 Z" fill="var(--mint)"/>
  </svg>

  <div class="brand">
    <span class="brand__dot"></span>
    <span class="brand__name">Corvin<br>Pediatric Smiles</span>
  </div>

  <div class="details">
    <div class="details__name">Tamsin Vetrakovich, DDS</div>
    <div class="details__title">Board Certified Pediatric Dentist</div>
    <div class="details__address">42 Brambury Ln, Ste 208<br>Wellesley, MA 02481</div>
    <ul class="details__contacts">
      <li><svg viewBox="0 0 24 24"><path d="M6.6 10.8a15 15 0 0 0 6.6 6.6l2.2-2.2c.3-.3.7-.4 1-.2 1.1.4 2.3.6 3.6.6.6 0 1 .4 1 1V20c0 .6-.4 1-1 1A17 17 0 0 1 3 4c0-.6.4-1 1-1h3.5c.6 0 1 .4 1 1 0 1.3.2 2.5.6 3.6.1.3 0 .7-.2 1z"/></svg>(617) 555-0148)</li>
      <li><svg viewBox="0 0 24 24"><path d="M6 2h10l2 2v5H6zM4 10h16a2 2 0 0 1 2 2v6h-4v4H6v-4H2v-6a2 2 0 0 1 2-2zm4 7v3h8v-3z"/></svg>(617) 555-0193</li>
      <li><svg viewBox="0 0 24 24"><path d="M2 5h20v14H2zm2 2v.5l8 5 8-5V7l-8 5z"/></svg>info@corvinpediatricsmiles.example</li>
    </ul>
  </div>

  <div class="website">www.corvinpediatricsmiles.example</div>
</section>

</body>
</html>
```